Business Card Design Project

Company name will be Tolvan Crest (named after my black lab and his fraying muzzle) Business is in the body armor, Security product industry servicing the state, local, and federal law enforcement markets. I want a more formal and serious logo for both business cards and letterhead

```html
<!DOCTYPE html>
<html lang="en">
<head>
<meta charset="utf-8">
<title>Tolvan Crest – Business Card</title>
<link rel="stylesheet" href="https://fonts.googleapis.com/css2?family=Dosis:wght@300;400;700&display=swap">
<style>
  :root {
    --stage: #3b3b3b;
    --card: #231c19;
    --ink-light: #e6e6e6;
    --ink-mid: #bdbdbd;
    --rule: #8a8583;
    --mark: #b8b8b8;
  }
  * { margin: 0; padding: 0; box-sizing: border-box; }
  html, body {
    width: 1200px;
    height: 751px;
    overflow: hidden;
    background: var(--stage);
    font-family: "Dosis", sans-serif;
  }
  .canvas {
    position: relative;
    width: 1200px;
    height: 751px;
  }
  .card {
    position: absolute;
    background: var(--card);
  }

  /* Front face */
  .card-front {
    left: 0; top: 29px;
    width: 687px; height: 398px;
  }
  .front-mark {
    position: absolute;
    left: 243px; top: 54px;
    width: 208px; height: 208px;
    border-radius: 50%;
    background: var(--mark);
  }
  .front-name {
    position: absolute;
    left: 0; width: 694px;
    top: 276px;
    text-align: center;
    font-weight: 700;
    font-size: 46px;
    letter-spacing: -0.5px;
    color: var(--ink-light);
  }

  /* Back face */
  .card-back {
    left: 463px; top: 324px;
    width: 690px; height: 396px;
  }
  .person {
    position: absolute;
    right: 426px; top: 154px;
    text-align: right;
  }
  .person-name {
    font-weight: 300;
    font-size: 23px;
    color: var(--ink-light);
    padding: 0 2px 4px 0;
    border-bottom: 1px solid var(--rule);
  }
  .person-role {
    margin-top: 6px;
    font-weight: 300;
    font-size: 20px;
    color: var(--ink-mid);
  }
  .divider {
    position: absolute;
    left: 286px; top: 100px;
    width: 1px; height: 187px;
    background: linear-gradient(to bottom, transparent, var(--rule) 20%, var(--rule) 80%, transparent);
  }
  .contact {
    position: absolute;
    left: 303px; top: 131px;
    list-style: none;
  }
  .contact li {
    display: flex;
    align-items: flex-start;
    font-weight: 300;
    font-size: 20px;
    line-height: 27px;
    color: var(--ink-mid);
  }
  .contact .icon {
    width: 20px; height: 20px;
    margin: 4px 10px 0 0;
    flex: none;
  }
  .back-brand {
    position: absolute;
    right: 28px; bottom: 30px;
    display: flex;
    align-items: center;
    gap: 10px;
  }
  .back-brand .dot {
    width: 28px; height: 28px;
    border-radius: 50%;
    background: var(--mark);
  }
  .back-brand .wordmark {
    font-weight: 700;
    font-size: 27px;
    color: var(--ink-light);
  }
</style>
</head>
<body>
<main class="canvas">
  <section class="card card-front" aria-label="Card front">
    <div class="front-mark"></div>
    <div class="front-name">Tolvan Crest</div>
  </section>

  <section class="card card-back" aria-label="Card back">
    <div class="person">
      <div class="person-name">Corin Haldane</div>
      <div class="person-role">Rep Principal</div>
    </div>
    <div class="divider"></div>
    <ul class="contact">
      <li>
        <svg class="icon" viewBox="0 0 20 20" aria-hidden="true">
          <circle cx="10" cy="10" r="8" fill="#cfcfcf"/>
          <circle cx="10" cy="10" r="3.5" fill="#6d6d6d"/>
        </svg>
        <span>1470 Harbor Row East<br>Marlow Point, FL 32091</span>
      </li>
      <li>
        <svg class="icon" viewBox="0 0 20 20" aria-hidden="true">
          <rect x="6" y="1" width="8" height="18" rx="1.5" fill="#cfcfcf"/>
          <rect x="7.5" y="3.5" width="5" height="6" fill="#6d6d6d"/>
        </svg>
        <span>555-204-7316</span>
      </li>
      <li>
        <svg class="icon" viewBox="0 0 20 20" aria-hidden="true">
          <rect x="2" y="3" width="16" height="11" rx="1" fill="#cfcfcf"/>
          <rect x="3.5" y="4.5" width="13" height="8" fill="#f2f2f2"/>
          <rect x="8" y="14" width="4" height="3" fill="#cfcfcf"/>
          <rect x="5.5" y="17" width="9" height="1.5" fill="#cfcfcf"/>
        </svg>
        <span>chaldane@mailbox.test</span>
      </li>
    </ul>
    <div class="back-brand">
      <div class="dot"></div>
      <div class="wordmark">Tolvan Crest</div>
    </div>
  </section>
</main>
</body>
</html>
```